Quorvex business card design

create modern and tech looking business card that is clean but effectively communciates that we are a cloud communications company.
Should have at minimum:
Employee Name
Postion
Phone Number
Email
website
create modern and tech looking business card that is clean but effectively communciates that we are a cloud communications company. We have two logo color schemes (attached) so would like to see designs both ways
Should have at minimum:
Employee Name
Postion
Phone Number
Email
website

```html
<!DOCTYPE html>
<html lang="en">
<head>
<meta charset="utf-8">
<title>Quorvex business card</title>
<link href="https://fonts.googleapis.com/css2?family=Montserrat:wght@400;500;600&display=swap" rel="stylesheet">
<style>
  :root {
    --canvas-bg: #eeecef;
    --card-bg: #ffffff;
    --card-back-bg: #f8f9f9;
    --ink: #3b3b3d;
    --ink-soft: #59595c;
    --lime: #8cc63f;
    --sky: #29b6e0;
    --slate: #4a4a4e;
  }
  * { box-sizing: border-box; margin: 0; padding: 0; }
  html, body { width: 1200px; height: 750px; overflow: hidden; }
  body {
    background: var(--canvas-bg);
    font-family: "Montserrat", sans-serif;
    color: var(--ink);
    position: relative;
  }
  .card {
    position: absolute;
    top: 225px;
    width: 520px;
    height: 300px;
    border-radius: 28px;
    overflow: hidden;
    box-shadow: 0 6px 18px rgba(0,0,0,0.12);
  }
  .card--front { left: 60px; background: var(--card-bg); }
  .card--back { left: 620px; background: var(--card-back-bg); }

  .stripe-band {
    position: absolute;
    inset: 0;
    background: linear-gradient(135deg, var(--lime) 0%, var(--sky) 45%, var(--slate) 75%, var(--lime) 100%);
  }
  .card--front .stripe-band--left { clip-path: polygon(0 0, 20% 0, 7% 100%, 0 100%); }
  .card--front .stripe-band--right { clip-path: polygon(93% 0, 100% 0, 100% 100%, 80% 100%); }
  .card--back .stripe-band--right { clip-path: polygon(89% 0, 100% 0, 100% 100%, 75% 100%); }

  .wordmark {
    position: absolute;
    display: flex;
    align-items: center;
    gap: 12px;
    font-weight: 500;
    color: var(--ink);
    letter-spacing: 0.08em;
    text-transform: uppercase;
  }
  .wordmark__square { background: var(--lime); flex: none; }
  .card--front .wordmark { left: 50%; top: 50%; transform: translate(-50%, -50%); font-size: 40px; }
  .card--front .wordmark__square { width: 34px; height: 34px; }
  .card--back .wordmark { right: 96px; top: 46px; font-size: 24px; }
  .card--back .wordmark__square { width: 22px; height: 22px; }

  .contact-block { position: absolute; left: 36px; bottom: 34px; width: 300px; }
  .contact-block__rule { height: 1px; background: var(--lime); width: 290px; margin-bottom: 12px; }
  .person-name { font-size: 24px; font-weight: 400; letter-spacing: 0.04em; line-height: 1; }
  .person-name__first { color: var(--lime); }
  .person-role { font-size: 12px; color: var(--ink-soft); margin-top: 4px; }
  .address { font-size: 11px; text-transform: uppercase; margin-top: 14px; line-height: 1.4; color: var(--ink); }
  .contact-list { list-style: none; margin-top: 10px; }
  .contact-list li { display: flex; align-items: center; gap: 8px; font-size: 11px; line-height: 1.75; color: var(--ink); }
  .contact-list svg { width: 11px; height: 11px; flex: none; }
</style>
</head>
<body>
  <section class="card card--front" aria-label="Card front">
    <div class="stripe-band stripe-band--left" role="img" aria-label="Diagonal band of green, blue and grey dash pattern"></div>
    <div class="stripe-band stripe-band--right" role="img" aria-label="Diagonal band of green, blue and grey dash pattern"></div>
    <div class="wordmark"><span class="wordmark__square"></span>Quorvex</div>
  </section>

  <section class="card card--back" aria-label="Card back">
    <div class="stripe-band stripe-band--right" role="img" aria-label="Diagonal band of green, blue and grey dash pattern"></div>
    <div class="wordmark"><span class="wordmark__square"></span>Quorvex</div>

    <div class="contact-block">
      <div class="contact-block__rule"></div>
      <h1 class="person-name"><span class="person-name__first">RHEA</span> LINDQVIST</h1>
      <p class="person-role">Graphic Designer</p>
      <p class="address">48 Meridian Loop 12<br>Ashcombe, NV 30218</p>
      <ul class="contact-list">
        <li>
          <svg viewBox="0 0 12 12" aria-hidden="true"><path d="M3 1l2 2.5-1.2 1.2a7 7 0 0 0 3.5 3.5L8.5 7 11 9l-1.5 2C5 11 1 7 1 2.5z" fill="none" stroke="#8cc63f" stroke-width="1"/></svg>
          1-555-210-4470
        </li>
        <li>
          <svg viewBox="0 0 12 12" aria-hidden="true"><rect x="1" y="2.5" width="10" height="7" fill="none" stroke="#8cc63f" stroke-width="1"/><path d="M1 2.5l5 4 5-4" fill="none" stroke="#8cc63f" stroke-width="1"/></svg>
          hello@quorvexcloud.com
        </li>
        <li>
          <svg viewBox="0 0 12 12" aria-hidden="true"><circle cx="6" cy="6" r="5" fill="none" stroke="#8cc63f" stroke-width="1"/><ellipse cx="6" cy="6" rx="2.2" ry="5" fill="none" stroke="#8cc63f" stroke-width="1"/><path d="M1 6h10" stroke="#8cc63f" stroke-width="1"/></svg>
          www.quorvexcloud.com
        </li>
      </ul>
    </div>
  </section>
</body>
</html>
```